Awesome Dessert Baker needs Sticker Design

My wife is an incredible baker. She specializes in desserts and everyone that tastes her baked goods has told her to start selling them. She recently decided to go into business and just through word of mouth and her reputation she is already getting steady orders.

She is looking to have a sticker developed to put on her cake boxes and packaging.

She wants the following:
1. Colors to be used- hot pink, purple, white
2. Want a sleek, modern design and style incorporating following:
name: Whisked by Nora
tel: 646 382 1074
email: nora@whiskedbynora.example

**no old fashion baking references like rolling pins, aprons, ect.

We want the sticker to be very appealing and eye catching that will further promote her image and business.

Industry/Entity Type

Fashion

Requirements
Must have
• Must contain the following information:

Whisked by Nora
646 382 1074 (please make small and discreet)
nora@whiskedbynora.example (please make small and discreet)
Should not have
• **no old fashion baking references like rolling pins, aprons, ect.

```html
<!DOCTYPE html>
<html lang="en">
<head>
<meta charset="utf-8">
<title>Whisked by Nora – Sticker</title>
<link rel="stylesheet" href="https://fonts.googleapis.com/css2?family=Baloo+2:wght@800&family=Arimo:wght@700&display=swap">
<style>
  :root {
    --hot-pink: #dd137f;
    --plum: #9a3f7d;
    --white: #ffffff;
    --edge: #b3b3b3;
  }
  * { margin: 0; padding: 0; box-sizing: border-box; }
  html, body {
    width: 1200px;
    height: 920px;
    overflow: hidden;
    background: var(--white);
  }
  .sticker-canvas {
    position: relative;
    width: 1200px;
    height: 920px;
    background: var(--white);
    border: 1px solid var(--edge);
  }
  .sticker-outline {
    position: absolute;
    inset: 0;
    width: 1200px;
    height: 920px;
  }
  .sticker-outline path {
    fill: var(--white);
    stroke: var(--hot-pink);
    stroke-width: 19;
    stroke-linejoin: miter;
    stroke-miterlimit: 12;
  }
  .contact-block {
    position: absolute;
    left: 0;
    width: 1186px;
    text-align: center;
    color: var(--plum);
    white-space: nowrap;
    line-height: 1;
  }
  .business-name {
    top: 366px;
    font-family: "Baloo 2", sans-serif;
    font-weight: 800;
    font-size: 60px;
    letter-spacing: 0.5px;
  }
  .phone {
    top: 458px;
    font-family: "Arimo", sans-serif;
    font-weight: 700;
    font-size: 29px;
  }
  .email {
    top: 506px;
    font-family: "Arimo", sans-serif;
    font-weight: 700;
    font-size: 26px;
  }
</style>
</head>
<body>
  <main class="sticker-canvas">
    <svg class="sticker-outline" viewBox="0 0 899 689" aria-hidden="true">
      <path d="M449,62 C400,110 300,150 240,200 C170,260 160,320 215,375 L165,430 L235,440 L205,500 L270,505 L255,565 L320,555 L330,612 L390,592 L420,635 L455,598 L490,635 L520,595 L575,615 L580,560 L645,570 L625,510 L695,505 L665,448 L735,435 L685,375 C740,320 730,260 660,200 C600,150 500,110 449,62 Z"/>
    </svg>
    <p class="contact-block business-name">name: Whisked by Nora</p>
    <p class="contact-block phone">tel: 646 382 1074</p>
    <p class="contact-block email">email: nora@whiskedbynora.example</p>
  </main>
</body>
</html>
```